Construction Company Website Design

I need a Website Design for a Construction Company. I have attached logo and business card design files (a.i) to match styles and text for the website. I will need design for 3 pages:
1. A Home page
2. A secondary page (will be different information pages)
3. A contact page with submision form
Website to look professional and match the 'theme' across all pages, using main colours / reverse colours as per design files. Must be clear it is a construction related website without being over the top. Happy for the construction related details (whether that be images/outlines/backgrounds etc to be fairly subtle and not overbearing on the contect of the pages. It will be the content that will be most important, not the images within.

Content has not yet been fully completed but attached is a site map. Each page will need a space for the insertion of the relevant heading and associated content for that particular page. Example can be used as per attached map. If it is preferable to have content completed for this to be a more succesful project please advise and I will complete and submit.

Target Market(s)

Clients for potential construction projects. These could be a range of people. All would be very professional, well educated and put a substantial expection on the quality of website provided.

Industry/Entity Type

Construction

Number of Pages Required

3 page

Font styles to use
Serif
Sans Serif
Other font styles liked:
• fonts preferable as per design files provided unless designer beleives a different font would suit better

Requirements
Must have
• Colour scheme to match logo and business card files provided. Fonts that match as per provided files. Pages must be consistent with the theme carrying across all pages. All pages must have contact details at the bottom of the page.
• Contents of page 1 - 'Home page': multiple tab options / logo link
• Contents of page 2 - 'Secondary page': Top and side navigation / area for information and/or images.
• Contents of page - 'Contact us page': Top and side navigation / Submission form / area for logos such as linkdin, facebook etc.
Nice to have
• Would be good to have a or some generic construction related images - outlines / shadows / effects etc. These might be background images or outlines related to the relevant industry and are consistent across the pages. Could be outlines of buildings, images of men with hardhats etc etc. Good to see colour scheme as per design files used
Should not have
• No pictures of houses. Generally no photos. If any imagery of people must not show faces/details.

```html
<!DOCTYPE html>
<html lang="en">
<head>
<meta charset="utf-8">
<title>Kestrel Build – Home</title>
<link rel="stylesheet" href="https://fonts.googleapis.com/css2?family=Rajdhani:wght@500;600;700&family=Russo+One&family=Mulish:wght@400;600;700&display=swap">
<style>
:root{
  --blue:#0aa3e6;
  --blue-dark:#0784c0;
  --ink:#2f3438;
  --text:#4a4f54;
  --muted:#8a9096;
  --dark:#222426;
  --dark-2:#2c2e31;
  --footer:#2b2c2e;
  --light:#e8eef1;
  --card:#f1f2f3;
  --white:#ffffff;
}
*{box-sizing:border-box;margin:0;padding:0}
html,body{width:1200px;height:2514px;overflow:hidden}
body{position:relative;background:var(--white);font-family:"Mulish",Arial,sans-serif;color:var(--text)}
.abs{position:absolute}
.btn{position:absolute;display:flex;align-items:center;justify-content:center;gap:6px;height:30px;background:var(--blue);color:var(--white);font:700 11px "Rajdhani",sans-serif;letter-spacing:.5px;text-transform:uppercase}
.btn svg{width:12px;height:12px}
.section-title{position:absolute;left:0;width:1200px;text-align:center;font:600 26px "Rajdhani",sans-serif;color:var(--ink);letter-spacing:.5px}
.section-title::after{content:"";display:block;width:60px;height:2px;background:var(--blue);margin:10px auto 0}

/* header */
.site-header{top:0;left:0;width:1200px;height:74px;background:var(--white)}
.brand{left:148px;top:22px;display:flex;align-items:center;gap:10px;font:600 20px "Rajdhani",sans-serif;color:var(--ink);letter-spacing:1px}
.brand .mark{width:14px;height:14px;background:var(--blue)}
.main-nav{left:390px;top:24px;display:flex;gap:6px}
.main-nav a{font:500 13px "Rajdhani",sans-serif;color:var(--ink);padding:4px 8px;text-transform:uppercase;text-decoration:none}
.main-nav a.active{background:var(--blue);color:var(--white)}
.header-phone{left:938px;top:25px;display:flex;align-items:center;gap:8px;font:600 16px "Rajdhani",sans-serif;color:var(--ink)}

/* hero */
.hero{top:74px;left:0;width:1200px;height:437px;background:linear-gradient(115deg,#3a1d2a 0%,#a2423a 25%,#e9a25b 45%,#f6e2c4 58%,#c9a49a 78%,#4a3340 100%)}
.hero-title{top:226px;left:0;width:1200px;text-align:center;font:40px "Russo One",sans-serif;color:#111}
.hero-sub{top:272px;left:0;width:1200px;text-align:center;font:400 24px "Mulish",sans-serif;color:#3b3030}
.hero-arrow{width:38px;height:38px;background:rgba(0,0,0,.6);top:272px;display:flex;align-items:center;justify-content:center}

/* welcome */
.welcome-text{left:240px;top:622px;width:720px;text-align:center;font:400 11.5px/17px "Mulish",sans-serif;color:var(--text)}
.welcome-title{top:558px}
.welcome-title b{font-weight:700}

/* services */
.services{top:816px;left:0;width:1200px;height:692px;background:radial-gradient(ellipse at 50% 60%,#3c3f43 0%,var(--dark) 70%)}
.service{position:absolute;top:922px;width:191px}
.service.featured{background:var(--white);box-shadow:0 4px 16px rgba(0,0,0,.4);padding:6px;width:203px;height:321px;margin-left:-6px}
.service .thumb{height:145px}
.service h3{margin-top:22px;font:700 15px "Rajdhani",sans-serif;color:var(--white);text-transform:uppercase;letter-spacing:.4px}
.service p{margin-top:10px;font:400 10.5px/17px "Mulish",sans-serif;color:#d8dadc}
.service.featured h3{color:var(--ink)}
.service.featured p{color:var(--text)}
.service .btn{position:relative;margin-top:18px;width:107px}

.projects{top:1341px;left:200px;width:800px;height:208px;display:flex}
.projects-intro{width:199px;height:208px;background:var(--blue);padding:20px 18px;color:var(--white)}
.projects-intro h2{font:700 24px/23px "Rajdhani",sans-serif;text-transform:uppercase}
.projects-intro p{margin-top:14px;font:400 10.5px/16px "Mulish",sans-serif}
.projects-intro .btn{position:relative;margin-top:14px;width:106px;background:var(--white);color:var(--blue)}
.project{width:200px;height:208px;position:relative;border-left:2px solid var(--dark)}
.project .thumb{height:168px}
.project .caption{height:40px;background:#000;color:var(--blue);font:600 11px "Mulish",sans-serif;display:flex;align-items:center;justify-content:center}

/* testimonials */
.testimonial{position:absolute;top:1663px;width:390px;height:149px;background:var(--card);padding:16px 20px}
.testimonial p{font:400 10.5px/18px "Mulish",sans-serif;color:var(--text)}
.testimonial h4{margin-top:10px;font:700 12px "Mulish",sans-serif;color:var(--ink)}
.testimonial small{font:400 10px "Mulish",sans-serif;color:var(--muted)}
.avatar{position:absolute;right:26px;bottom:-20px;width:50px;height:50px;border-radius:50%;border:3px solid var(--white);background:linear-gradient(#c9a488,#7c5a44)}
.nav-chevron{position:absolute;top:1710px}

/* news */
.news-band{top:1891px;left:0;width:1200px;height:196px;background:var(--light)}
.news-card{position:absolute;top:2010px;width:247px;height:189px;background:var(--white);border-top:6px solid var(--blue);padding:18px 20px;border-bottom:1px solid #e2e4e6}
.news-card.featured{box-shadow:0 6px 18px rgba(0,0,0,.15)}
.news-card .date{font:600 9.5px "Mulish",sans-serif;color:var(--blue)}
.news-card h3{margin-top:8px;font:700 12px/18px "Mulish",sans-serif;color:var(--ink)}
.news-card p{margin-top:12px;font:400 10.5px/18px "Mulish",sans-serif;color:var(--text)}

/* footer */
.site-footer{top:2301px;left:0;width:1200px;height:213px;background:var(--footer);color:#e6e7e8}
.footer-brand{left:188px;top:2338px;display:flex;align-items:center;gap:10px;font:600 20px "Rajdhani",sans-serif;color:var(--white);letter-spacing:1px}
.footer-brand .mark{width:14px;height:14px;background:var(--blue)}
.copyright{left:186px;top:2471px;font:400 10px "Mulish",sans-serif;color:#cfd1d3}
.footer-col h4{font:700 12px "Mulish",sans-serif;text-transform:uppercase;color:var(--white);margin-bottom:12px}
.footer-col li{list-style:none;font:400 10.5px/18px "Mulish",sans-serif}
.contact-row{display:flex;gap:12px;font:400 10.5px/16px "Mulish",sans-serif;margin-bottom:14px}
.contact-row svg{flex:none;margin-top:2px}
.socials{display:flex;gap:4px}
.socials span{width:28px;height:28px;border:2px solid var(--white);border-radius:50%}
</style>
</head>
<body>

<header class="abs site-header">
  <div class="abs brand"><span class="mark"></span>Kestrel Build</div>
  <nav class="abs main-nav">
    <a class="active">Home</a><a>About Us</a><a>Services</a><a>Projects</a><a>Culture</a><a>News</a><a>Contact</a>
  </nav>
  <div class="abs header-phone">
    <svg width="18" height="18" viewBox="0 0 24 24" fill="none" stroke="var(--blue)" stroke-width="2"><path d="M22 16.9v3a2 2 0 0 1-2.2 2 19.8 19.8 0 0 1-8.6-3.1 19.5 19.5 0 0 1-6-6A19.8 19.8 0 0 1 2.1 4.2 2 2 0 0 1 4.1 2h3a2 2 0 0 1 2 1.7c.1 1 .4 1.9.7 2.8a2 2 0 0 1-.5 2.1L8 9.9a16 16 0 0 0 6 6l1.3-1.3a2 2 0 0 1 2.1-.4c.9.3 1.8.6 2.8.7a2 2 0 0 1 1.7 2z"/></svg>
    0400-123-456
  </div>
</header>

<section class="abs hero" role="img" aria-label="Upward view of glass office towers in warm sunset light"></section>
<div class="abs hero-arrow" style="left:21px"><svg width="12" height="12" viewBox="0 0 12 12"><path d="M8 1 3 6l5 5" stroke="#fff" stroke-width="2" fill="none"/></svg></div>
<div class="abs hero-arrow" style="left:1141px"><svg width="12" height="12" viewBox="0 0 12 12"><path d="m4 1 5 5-5 5" stroke="#fff" stroke-width="2" fill="none"/></svg></div>
<h1 class="abs hero-title">LOREM IPSUM DOLOR</h1>
<p class="abs hero-sub">Ut enim ad minim veniam</p>
<a class="btn" style="left:547px;top:332px;width:106px">Read more <svg viewBox="0 0 12 12"><path d="M1 6h9M6 2l4 4-4 4" stroke="#fff" stroke-width="1.8" fill="none"/></svg></a>

<h2 class="section-title welcome-title" style="font-weight:500">WELCOME TO <b>KESTREL BUILD</b></h2>
<p class="abs welcome-text">Lorem ipsum dolor sit amet, consectetur adipiscing elit, sed do eiusmod tempor incididunt ut labore et dolore magna aliqua. Ut enim ad minim veniam, quis nostrud exercitation ullamco laboris nisi ut aliquip ex ea commodo consequat. Duis aute irure dolor in reprehenderit in voluptate velit esse cillum dolore eu fugiat nulla pariatur. Excepteur sint occaecat cupidatat non proident, sunt in culpa qui officia deserunt mollit anim id est laborum. Sed ut perspiciatis unde omnis iste natus error sit voluptatem accusantium doloremque laudantium, totam rem aperiam, eaque ipsa quae ab illo inventore veritatis et quasi architecto beatae vitae dicta sunt explicabo.</p>
<a class="btn" style="left:547px;top:739px;width:106px">Read more <svg viewBox="0 0 12 12"><path d="M1 6h9M6 2l4 4-4 4" stroke="#fff" stroke-width="1.8" fill="none"/></svg></a>

<section class="abs services" role="img" aria-label="Dark photo of a stairway in a building interior"></section>
<h2 class="section-title" style="top:862px;color:var(--white)">OUR SERVICES</h2>

<article class="service" style="left:200px">
  <div class="thumb" role="img" aria-label="Glass commercial towers against blue sky" style="background:linear-gradient(160deg,#cfe6f7,#3d86c7 60%,#1e4f8a)"></div>
  <h3>Commercial</h3>
  <p>Lorem ipsum dolor sit amet, consectetur adipiscing elit, sed do eiusmod tempor incididunt ut labore et dolore magna aliqua.</p>
  <a class="btn">Read more <svg viewBox="0 0 12 12"><path d="M1 6h9M6 2l4 4-4 4" stroke="#fff" stroke-width="1.8" fill="none"/></svg></a>
</article>
<article class="service" style="left:402px">
  <div class="thumb" role="img" aria-label="Modern residential building rendering" style="background:linear-gradient(160deg,#e9ecef,#b7bfc8 60%,#8d98a3)"></div>
  <h3>Residential</h3>
  <p>Lorem ipsum dolor sit amet, consectetur adipiscing elit, sed do eiusmod tempor incididunt ut labore et dolore magna aliqua.</p>
  <a class="btn">Read more <svg viewBox="0 0 12 12"><path d="M1 6h9M6 2l4 4-4 4" stroke="#fff" stroke-width="1.8" fill="none"/></svg></a>
</article>
<article class="service featured" style="left:605px;top:916px">
  <div class="thumb" role="img" aria-label="Worker in safety vest on a ladder doing maintenance" style="background:linear-gradient(160deg,#f1f2f2,#c7cccf 55%,#8e9aa6)"></div>
  <h3>Building Maintenance</h3>
  <p>Lorem ipsum dolor sit amet, consectetur adipiscing elit, sed do eiusmod tempor incididunt ut labore et dolore magna aliqua.</p>
  <a class="btn">Read more <svg viewBox="0 0 12 12"><path d="M1 6h9M6 2l4 4-4 4" stroke="#fff" stroke-width="1.8" fill="none"/></svg></a>
</article>
<article class="service" style="left:810px">
  <div class="thumb" role="img" aria-label="Hands reviewing project plans at a desk" style="background:linear-gradient(160deg,#f3d9b8,#d49a63 55%,#8a5a3a)"></div>
  <h3>Project Management</h3>
  <p>Lorem ipsum dolor sit amet, consectetur adipiscing elit, sed do eiusmod tempor incididunt ut labore et dolore magna aliqua.</p>
  <a class="btn">Read more <svg viewBox="0 0 12 12"><path d="M1 6h9M6 2l4 4-4 4" stroke="#fff" stroke-width="1.8" fill="none"/></svg></a>
</article>

<section class="abs projects">
  <div class="projects-intro">
    <h2>Recent<br>Projects</h2>
    <p>Lorem ipsum dolor sit amet, consectetur adipiscing elit, sed do eiusmod tempor.</p>
    <a class="btn">View more <svg viewBox="0 0 12 12"><path d="M1 6h9M6 2l4 4-4 4" stroke="var(--blue)" stroke-width="1.8" fill="none"/></svg></a>
  </div>
  <div class="project"><div class="thumb" role="img" aria-label="Apartment building with balconies" style="background:linear-gradient(170deg,#8cc3ea,#dfe6ea 55%,#6f8a6a)"></div><div class="caption">Lorem ipsum dolor</div></div>
  <div class="project"><div class="thumb" role="img" aria-label="Modern apartment block against blue sky" style="background:linear-gradient(170deg,#5aa6e3,#b08a5e 55%,#3f3a36)"></div><div class="caption">Lorem ipsum dolor</div></div>
  <div class="project"><div class="thumb" role="img" aria-label="Tall residential tower" style="background:linear-gradient(170deg,#9fd0f2,#d9dadb 55%,#6a6b6d)"></div><div class="caption">Lorem ipsum dolor</div></div>
</section>

<h2 class="section-title" style="top:1597px">TESTIMONIALS</h2>
<svg class="nav-chevron" style="left:155px" width="26" height="46" viewBox="0 0 26 46"><path d="M24 2 3 23l21 21" stroke="#b9d8e8" stroke-width="2" fill="none"/></svg>
<svg class="nav-chevron" style="left:1018px" width="26" height="46" viewBox="0 0 26 46"><path d="m2 2 21 21L2 44" stroke="var(--blue)" stroke-width="2" fill="none"/></svg>
<article class="testimonial" style="left:200px">
  <p>"Lorem ipsum dolor sit amet, consectetur adipiscing elit, sed do eiusmod tempor incididunt ut labore et dolore magna aliqua. Ut enim ad minim veniam, quis nostrud exercitation ullamco laboris nisi ut aliquip ex ea commodo consequat."</p>
  <h4>Adam Reed</h4><small>Lorem ipsum</small>
  <div class="avatar" role="img" aria-label="Client portrait"></div>
</article>
<article class="testimonial" style="left:610px">
  <p>"Lorem ipsum dolor sit amet, consectetur adipiscing elit, sed do eiusmod tempor incididunt ut labore et dolore magna aliqua. Ut enim ad minim veniam, quis nostrud exercitation ullamco laboris nisi ut aliquip ex ea commodo consequat."</p>
  <h4>John Doe</h4><small>Lorem ipsum</small>
  <div class="avatar" role="img" aria-label="Client portrait"></div>
</article>

<div class="abs news-band"></div>
<h2 class="section-title" style="top:1938px">LATEST NEWS</h2>
<article class="news-card" style="left:210px">
  <div class="date">APR 15, 2018</div>
  <h3>Lorem ipsum dolor sit amet, consectetur adipiscing elit</h3>
  <p>Duis aute irure dolor in reprehenderit in voluptate velit esse cillum dolore eu fugiat nulla pariatur. Excepteur sint occaecat cupidatat non proident. [...]</p>
</article>
<article class="news-card featured" style="left:476px">
  <div class="date">APR 15, 2018</div>
  <h3>Lorem ipsum dolor sit amet, consectetur adipiscing elit</h3>
  <p>Duis aute irure dolor in reprehenderit in voluptate velit esse cillum dolore eu fugiat nulla pariatur. Excepteur sint occaecat cupidatat non proident. [...]</p>
</article>
<article class="news-card" style="left:742px">
  <div class="date">APR 15, 2018</div>
  <h3>Lorem ipsum dolor sit amet, consectetur adipiscing elit</h3>
  <p>Duis aute irure dolor in reprehenderit in voluptate velit esse cillum dolore eu fugiat nulla pariatur. Excepteur sint occaecat cupidatat non proident. [...]</p>
</article>
<a class="btn" style="left:547px;top:2224px;width:106px">Read more <svg viewBox="0 0 12 12"><path d="M1 6h9M6 2l4 4-4 4" stroke="#fff" stroke-width="1.8" fill="none"/></svg></a>

<footer class="abs site-footer"></footer>
<div class="abs footer-brand"><span class="mark"></span>Kestrel Build</div>
<p class="abs copyright">© 2018 Kestrel Build. All Rights Reserved.</p>
<div class="abs footer-col" style="left:481px;top:2333px">
  <h4>Quick Links</h4>
  <ul><li>Home</li><li>About Us</li><li>Services</li><li>Projects</li><li>Culture</li><li>News</li><li>Contact</li></ul>
</div>
<div class="abs footer-col" style="left:595px;top:2333px">
  <h4>Contact</h4>
  <div class="contact-row"><svg width="14" height="14" viewBox="0 0 24 24" fill="none" stroke="#fff" stroke-width="2"><path d="M12 22s7-6.5 7-12a7 7 0 0 0-14 0c0 5.5 7 12 7 12z"/><circle cx="12" cy="10" r="2.5"/></svg><span>Kestrel Build Pty Limited<br>14 Harbour Lane<br>Westbrook 2100</span></div>
  <div class="contact-row" style="margin-top:18px"><svg width="14" height="14" viewBox="0 0 24 24" fill="none" stroke="#fff" stroke-width="2"><path d="M22 16.9v3a2 2 0 0 1-2.2 2 19.8 19.8 0 0 1-8.6-3.1 19.5 19.5 0 0 1-6-6A19.8 19.8 0 0 1 2.1 4.2 2 2 0 0 1 4.1 2h3a2 2 0 0 1 2 1.7c.1 1 .4 1.9.7 2.8a2 2 0 0 1-.5 2.1L8 9.9a16 16 0 0 0 6 6l1.3-1.3a2 2 0 0 1 2.1-.4c.9.3 1.8.6 2.8.7a2 2 0 0 1 1.7 2z"/></svg><span>0400 123 456</span></div>
  <div class="contact-row" style="margin-top:18px"><svg width="14" height="14" viewBox="0 0 24 24" fill="none" stroke="#fff" stroke-width="2"><rect x="3" y="5" width="18" height="14" rx="1"/><path d="m3 6 9 7 9-7"/></svg><span>info@kestrelbuild.com.au</span></div>
</div>
<div class="abs footer-col" style="left:809px;top:2333px">
  <h4>Stay in Touch</h4>
  <div class="socials"><span></span><span></span><span></span><span></span></div>
</div>

</body>
</html>
```